Heron Cove Sailing needs a flyer promoting sailing holidays on the Coral Lantern Shoals

Heron Cove Sailing is a private yacht charter company based in Sydney run by Mark & Jenny Dorst. We love sailing and our business allows us to share this passion with others. In winter 2015 (June - October) we're heading to Queensland, Australia to explore the Coral Lantern Shoals. We're offering sailing holidays on a large luxury yacht to small groups (max six guests on board, ideally four). We would like the design to complement our website (www.heroncovesailing-demo.com.au) and reflect our tagline "where sailing meets fun and relaxation". I have attached a design brief with more information, some photos of previous trips to QLD and two versions of our logo.

Target Market(s)

Target markets are
-Small families (kid friendly) or couples with an interest in sailing or potential interest in sailing or
- Individuals who are learning to sail or love sailing or adventure travellers

Age bracket for both groups is 30-50.

Small families/couples will be professionals with well-paid jobs where they need a holiday where most things are done for them to wind down. They have a sense of adventure and would be bored just sitting on the beach. They like healthy living, fresh food and exercise, especially water sports (ideally sailing)

Individuals most likely will be learning to sail or adventure travellers looking for a different way to spend a few days away. They will earn a good wage in middle management, most likely come from the corporate world.

Industry/Entity Type

Business

Font styles to use
Sans Serif

Colors
0355a3
fece3f

Requirements
Must have
• Our Logo, contact details - name, email, website and phone no.
• Our Tagline.
Nice to have
• Roam Ratings logo, Chatterbook reference

```html
<!DOCTYPE html>
<html lang="en">
<head>
<meta charset="utf-8">
<title>Heron Cove Sailing – Flyer</title>
<link rel="stylesheet" href="https://fonts.googleapis.com/css2?family=Oswald:wght@500;600&family=Libre+Baskerville:wght@400;700&family=Lato:wght@700&display=swap">
<style>
  :root {
    --navy: #0e2a6e;
    --royal: #0355a3;
    --deep: #071f5a;
    --gold: #e3b54e;
    --ink: #1b2f6b;
    --white: #ffffff;
  }
  * { margin: 0; padding: 0; box-sizing: border-box; }
  html, body { width: 981px; height: 1200px; overflow: hidden; background: #f2f2f2; }
  .flyer { position: relative; width: 981px; height: 1200px; background: var(--white); overflow: hidden; }

  .photo-sea { position: absolute; left: 0; top: 0; width: 567px; height: 520px;
    background: linear-gradient(180deg,
      #3a68b0 0%, #5a86c4 24%, #86a8d4 34.5%,
      #5d7f8a 35%, #2f5f9a 36%, #3d72ae 52%, #5f93bf 70%, #7aa7c4 85%, #5b88b2 100%); }
  .photo-dock { position: absolute; left: 567px; top: 0; width: 414px; height: 560px;
    background: linear-gradient(180deg,
      #5d95d8 0%, #8fbde6 22%, #b9d7ec 32%,
      #9a8a6a 33%, #7f7358 36%, #4f9fb4 37%, #6cc0c8 50%, #4bb0b8 58%, #7ec7c4 66%, #b7b49a 80%, #c9b690 100%); }

  .wave { position: absolute; left: 0; top: 0; width: 981px; height: 640px; }

  .logo-mark { position: absolute; left: 245px; top: 70px; width: 110px; height: 110px;
    border-radius: 50%; background: var(--white); }
  .brand { position: absolute; left: 20px; top: 218px; width: 560px; text-align: center;
    font-family: "Libre Baskerville", serif; font-weight: 400; color: var(--white);
    font-size: 58px; line-height: 1.08; letter-spacing: 4px; text-transform: uppercase; }

  .tagline { position: absolute; left: 47px; top: 478px; width: 486px; height: 158px; }
  .tagline svg { position: absolute; inset: 0; }
  .tagline-main, .tagline-sub { position: absolute; left: 0; width: 100%; text-align: center;
    font-family: "Oswald", sans-serif; text-transform: uppercase; }
  .tagline-main { top: 10px; font-size: 57px; font-weight: 600; color: var(--white); letter-spacing: 0.5px; line-height: 1.1; }
  .tagline-sub { top: 80px; font-size: 31px; font-weight: 500; color: var(--gold); letter-spacing: 0.3px; line-height: 1.1; }

  .beach-fade { position: absolute; left: 0; top: 870px; width: 567px; height: 260px;
    background: linear-gradient(180deg, rgba(220,224,230,0) 0%, #e1e4e9 40%, #cfd5dd 100%); }

  .offer { position: absolute; left: 31px; top: 700px; width: 505px;
    font-family: "Libre Baskerville", serif; font-weight: 700; color: var(--ink);
    font-size: 22px; line-height: 1.22; }
  .offer p + p { margin-top: 16px; }

  .moments { position: absolute; top: 945px; left: 0; width: 567px; height: 142px; }
  .moment { position: absolute; top: 0; width: 142px; height: 142px; border-radius: 50%;
    background: var(--navy); padding: 10px; }
  .moment span { display: block; width: 100%; height: 100%; border-radius: 50%; border: 3px solid var(--white); }
  .moment-1 { left: 39px; }
  .moment-1 span { background: linear-gradient(180deg, #6f9fd6 0%, #a9c7e6 38%, #8a8f7e 42%, #c9b48c 58%, #e2cfa6 100%); }
  .moment-2 { left: 228px; }
  .moment-2 span { background: linear-gradient(180deg, #5a84c0 0%, #a9bfd8 35%, #e8c996 48%, #7c8fa6 52%, #d8c29a 72%, #a48a66 100%); }
  .moment-3 { left: 410px; }
  .moment-3 span { background: linear-gradient(180deg, #7fb0de 0%, #a9cde8 18%, #4e8a6a 21%, #3fb7c4 26%, #7fd1d0 55%, #3a9fae 100%); }

  .story-panel { position: absolute; left: 567px; top: 640px; width: 414px; height: 489px;
    background: linear-gradient(180deg, #0a2f8a 0%, #0b3a9c 50%, #0355a3 100%); }
  .photo-crew { position: absolute; left: 567px; top: 905px; width: 414px; height: 224px;
    background: linear-gradient(180deg, rgba(3,85,163,0) 0%, #2b78c4 35%, #1f69b6 65%, #2a5f9e 100%); }
  .story { position: absolute; left: 590px; top: 628px; width: 360px; text-align: right;
    font-family: "Lato", sans-serif; font-weight: 700; color: var(--white); font-size: 18px; line-height: 1.3; }
  .story p + p { margin-top: 22px; }

  .contact-bar { position: absolute; left: 0; top: 1129px; width: 981px; height: 71px;
    font-family: "Lato", sans-serif; font-weight: 700; }
  .contact-phone { position: absolute; left: 0; top: 0; width: 567px; height: 71px; background: var(--navy);
    color: var(--white); font-size: 24px; display: flex; align-items: center; justify-content: center; gap: 10px; }
  .contact-phone svg { width: 22px; height: 22px; }
  .contact-web { position: absolute; left: 567px; top: 0; width: 414px; height: 71px; background: var(--white);
    color: var(--ink); font-size: 19px; display: flex; align-items: center; justify-content: center; }
</style>
</head>
<body>
<main class="flyer">
  <div class="photo-sea" role="img" aria-label="Calm blue sea under a clear sky with a small island on the horizon"></div>
  <div class="photo-dock" role="img" aria-label="Thatched jetty over clear turquoise water with kayaks on the sand and two children jumping"></div>

  <svg class="wave" viewBox="0 0 981 640" aria-hidden="true">
    <defs>
      <linearGradient id="band" x1="0" y1="0" x2="1" y2="0">
        <stop offset="0" stop-color="#0a2a78"/>
        <stop offset="1" stop-color="#0f3f9e"/>
      </linearGradient>
    </defs>
    <path d="M0,385 C260,330 620,380 981,470 L981,525 C640,455 280,420 0,455 Z" fill="url(#band)"/>
    <path d="M0,455 C280,420 640,455 981,525 L981,640 L0,640 Z" fill="#ffffff"/>
    <path d="M567,497 C720,512 860,530 981,545 L981,640 L567,640 Z" fill="#0a2f8a"/>
  </svg>

  <div class="logo-mark" aria-hidden="true"></div>
  <div class="brand">Heron Cove<br>Sailing</div>

  <div class="tagline">
    <svg viewBox="0 0 486 158" aria-hidden="true">
      <path d="M4,4 H482 V148 L243,126 L4,148 Z" fill="var(--navy)" stroke="#ffffff" stroke-width="6"/>
    </svg>
    <div class="tagline-main">Where Sailing</div>
    <div class="tagline-sub">Meets Fun and Relaxation</div>
  </div>

  <div class="beach-fade" role="img" aria-label="Soft faded white sand beach"></div>

  <section class="offer">
    <p>Escape to the Coral Lantern Shoals Skippered charters for 2-6 guests.</p>
    <p>There's plenty to do..Sailing, snorkelling, whale-watching, fishing to name a few,or you can just hang out in hammocks!</p>
  </section>

  <div class="moments">
    <div class="moment moment-1" role="img" aria-label="Guests relaxing on a beach log"><span></span></div>
    <div class="moment moment-2" role="img" aria-label="Yacht anchored off a beach at sunset"><span></span></div>
    <div class="moment moment-3" role="img" aria-label="Snorkeller over clear reef water"><span></span></div>
  </div>

  <div class="story-panel"></div>
  <div class="photo-crew" role="img" aria-label="Skipper and toddler in a life jacket with swimmers underwater behind"></div>
  <section class="story">
    <p>Heron Cove Sailing was established in 2010 and shows Sydney Harbour hundreds of people every year.</p>
    <p>Our goal is to give everyone the experience of sailing while enjoying the beauty of our surroundings and the company of the guests on board.</p>
    <p>We love sharing our passion for sailing and take great pleasure from sharing with others the enjoyment Heron Cove brings to us.</p>
  </section>

  <footer class="contact-bar">
    <div class="contact-phone">
      <span>Mark on</span>
      <svg viewBox="0 0 24 24" aria-hidden="true">
        <rect x="1" y="1" width="22" height="22" rx="5" fill="#ffffff"/>
        <path d="M8.2,5.5 L10,8.6 L8.6,10.2 C9.5,12.2 11.3,14.1 13.5,15.2 L15,13.8 L18.4,15.6 L17.6,18.2 C11.5,18.6 5.2,12.3 5.7,6.3 Z" fill="var(--navy)"/>
      </svg>
      <span>0412 555 018</span>
    </div>
    <div class="contact-web">www.heroncovesailing-demo.com.au</div>
  </footer>
</main>
</body>
</html>
```